Would need to a simple sticker for baby wipe. (Layout provided)

Hi guys,
I would need to design a removable sticker that located under the lid of baby wipe, please look at picture 1 then you will get what it is (the yellow oval). It just a sticker that consumer will removed at the beginning in order to take out the wipe.
-Picture 2 and 3: are some ideas from other competitors. As you could see, most are oval shapes, and the ideas are quite variety, some are very simple, some is more complicate.
-Picture 4: is my actual product.
-File "layout.AI" is where you could begin with (or not, if you want). I hope you could help to design a simple design, but still somehow match with the overall design of the product (which already have quite soft and colorful pastel).
Dimension is around 6x3 cm
The idea are totally freedom.
Thank you for your help

```html
<!DOCTYPE html>
<html lang="vi">
<head>
<meta charset="UTF-8">
<title>Nhãn nắp khăn ướt</title>
<link rel="stylesheet" href="https://fonts.googleapis.com/css2?family=Sriracha&display=swap">
<style>
  :root {
    --page-bg: #ffffff;
    --label-teal: #4996a6;
    --label-line: #ffffff;
    --text-white: #ffffff;
    --butterfly-blue: #6cc2dc;
  }
  html, body {
    margin: 0;
    padding: 0;
    width: 1200px;
    height: 1200px;
    overflow: hidden;
    background: var(--page-bg);
  }
  .canvas {
    display: block;
    width: 1200px;
    height: 1200px;
  }
  .label-body { fill: var(--label-teal); }
  .label-outline {
    fill: none;
    stroke: var(--label-line);
    stroke-width: 7;
  }
  .pull-arrow { fill: var(--text-white); }
  .label-text {
    font-family: "Sriracha", cursive;
    font-size: 118px;
    fill: var(--text-white);
    text-anchor: middle;
  }
  .butterfly-spot { fill: var(--butterfly-blue); }
</style>
</head>
<body>
<svg class="canvas" viewBox="0 0 1932 1932" xmlns="http://www.w3.org/2000/svg">
  <g class="lid-label">
    <path class="label-body"
      d="M545,614 H1250 C1390,614 1500,700 1558,795 H1565 A170,170 0 0 1 1565,1135 H1558 C1500,1240 1390,1318 1250,1318 H545 A352,352 0 0 1 545,614 Z"/>
    <path class="label-outline"
      d="M545,660 H1250 C1380,660 1470,735 1518,818 C1530,838 1550,843 1570,842 A124,124 0 0 1 1570,1090 C1550,1089 1530,1095 1518,1115 C1470,1200 1380,1272 1250,1272 H545 A306,306 0 0 1 545,660 Z"/>
    <path class="pull-arrow"
      d="M1530,965 L1602,894 V930 H1656 Q1672,965 1656,1000 H1602 V1036 Z"/>

    <g class="butterfly-spot" role="img" aria-label="Bướm trang trí màu xanh nhạt">
      <ellipse cx="1305" cy="790" rx="62" ry="48"/>
    </g>
    <g class="butterfly-spot" role="img" aria-label="Bướm trang trí màu xanh nhạt">
      <ellipse cx="378" cy="960" rx="62" ry="52"/>
    </g>
    <g class="butterfly-spot" role="img" aria-label="Bướm trang trí nhỏ màu xanh nhạt">
      <ellipse cx="1295" cy="1135" rx="36" ry="28"/>
    </g>

    <text class="label-text" x="915" y="932">Nên đóng kín nắp</text>
    <text class="label-text" x="885" y="1090">nhựa sau khi sử dụng</text>
  </g>
</svg>
</body>
</html>
```